VELDA Motorcycle Ad

We import a range of specialised high end competition Off-Road motorcycles from Spain. We have a new model out called the VELDA Kx340e which we would like a banner ad for. The main features we want to highlight on the new VELDA is the light weight (lightest on the market) BRAKMOR rear shock (Best on the market) & an industry leading 2 year warranty. We can supply images etc. tis is our first time using this service so not sure of the procedure.

```html
<!DOCTYPE html>
<html lang="en">
<head>
<meta charset="utf-8">
<title>NRTA Coffs Road Show Update</title>
<link rel="stylesheet" href="https://fonts.googleapis.com/css2?family=Didact+Gothic&family=Noto+Sans:wght@400;700&display=swap">
<style>
:root{
  --black:#000;
  --nav-red:#6e0000;
  --nav-line:#a33a3a;
  --title-red:#7a0000;
  --text:#3a3a3a;
  --meta:#9a9a9a;
  --link:#b00000;
  --side-tan:#d8cfae;
  --side-head:#c9c29c;
  --side-yellow:#ffd400;
  --social-blue:#3b5998;
  --ad-green:#2fb24a;
}
*{margin:0;padding:0;box-sizing:border-box}
html,body{width:1200px;height:900px;overflow:hidden;background:#fff}
body{position:relative;font-family:"Didact Gothic",sans-serif;color:var(--text)}
.site-header{position:absolute;left:0;top:0;width:1200px;height:216px;background:var(--black)}
.site-brand{position:absolute;left:-6px;top:60px;display:flex;align-items:center;gap:10px;color:#fff;font-family:"Noto Sans",sans-serif;font-weight:700;font-size:30px}
.site-brand .dot{width:26px;height:26px;border-radius:50%;background:#f2b600}
.banner-ad{position:absolute;left:232px;top:46px;width:936px;height:120px;border:2px solid #333;background:linear-gradient(90deg,#111 0%,#222 55%,#2c2c2c 100%);overflow:hidden;font-family:"Noto Sans",sans-serif}
.banner-ad .model{position:absolute;left:10px;top:6px;font-size:38px;font-weight:700;color:var(--ad-green);letter-spacing:1px}
.banner-ad ul{position:absolute;left:14px;top:60px;list-style:none;color:#fff;font-size:21px;font-weight:700;line-height:27px}
.banner-ad li::before{content:"•";margin-right:10px}
.banner-ad .photo{position:absolute;right:0;top:0;width:380px;height:116px;background:linear-gradient(110deg,#3a3a3a,#8a8a8a 45%,#2a2a2a)}
.main-nav{position:absolute;left:0;top:216px;width:1200px;height:64px;background:var(--nav-red);border-top:2px solid #4a0000;display:flex;font-family:"Noto Sans",sans-serif;font-size:27px;color:#fff}
.main-nav span{height:100%;display:flex;align-items:center;justify-content:center;border-right:2px solid var(--nav-line)}
.page-bg{position:absolute;left:0;top:280px;width:1096px;height:110px;background:linear-gradient(#dcdcdc,#fff)}
.breadcrumb{position:absolute;left:-12px;top:296px;font-size:26px;color:#555}
.article{position:absolute;left:-8px;top:372px;width:1096px}
.article-title{font-size:38px;color:var(--title-red);font-weight:400;padding-bottom:8px;border-bottom:2px solid #ccc;width:1000px;position:relative}
.tools{position:absolute;left:996px;top:388px;display:flex;gap:12px}
.meta{font-size:18px;color:var(--meta);margin-top:14px;line-height:20px}
.meta+.meta{margin-top:18px}
.article p{font-size:26px;line-height:41px;margin-top:14px;color:var(--text)}
.article p:first-of-type{margin-top:8px}
.article a{color:var(--link)}
.sidebar{position:absolute;left:1096px;top:280px;width:104px;height:620px;background:var(--side-tan);border-left:2px solid #c2b78d}
.social-box{position:absolute;left:12px;top:16px;width:100px;height:112px;background:#fff}
.social-box .head{height:50px;background:var(--social-blue);color:#fff;font-family:"Noto Sans",sans-serif;font-weight:700;font-size:28px;padding:6px 0 0 8px}
.social-box .badge{position:absolute;left:14px;top:58px;width:48px;height:48px;background:#111}
.latest-head{position:absolute;left:0;top:218px;width:104px;height:50px;background:linear-gradient(#ddd7b9,var(--side-head));font-family:"Noto Sans",sans-serif;font-weight:700;font-size:26px;color:#4a3a00;padding:8px 0 0 12px}
.latest-list{position:absolute;left:8px;top:276px;width:96px;height:344px;background:var(--side-yellow);list-style:none;font-family:"Noto Sans",sans-serif;font-size:24px;color:#5a0000;line-height:34px;padding:6px 0 0 0;overflow:hidden;white-space:nowrap}
.latest-list li{padding-left:12px}
.latest-list li.bullet::before{content:"▪";color:#b00000;margin-right:12px}
</style>
</head>
<body>
<header class="site-header">
  <div class="site-brand"><span>Ridge</span><span class="dot"></span></div>
  <aside class="banner-ad" aria-label="VELDA Kx340e advertisement">
    <div class="model">VELDA Kx340e</div>
    <ul>
      <li>LIGHT WEIGHT BRAKMOR REAR SHOCK</li>
      <li>INDUSTRY LEADING 2 YEAR WARRANTY</li>
    </ul>
    <div class="photo" role="img" aria-label="Close-up photo of the VELDA Kx340e engine and frame"></div>
  </aside>
</header>
<nav class="main-nav">
  <span style="width:66px">nts</span>
  <span style="width:184px">Forum</span>
  <span style="width:230px">Photo Gallery</span>
  <span style="width:134px">Admin</span>
  <span style="width:180px">Site Info</span>
  <span style="width:218px">Contact Us</span>
  <span style="width:188px;border-right:none">Site Search</span>
</nav>
<div class="page-bg"></div>
<div class="breadcrumb">Home</div>
<div class="tools">
  <svg width="28" height="28" viewBox="0 0 28 28"><rect x="4" y="10" width="20" height="12" rx="2" fill="#7a8aa8"/><rect x="8" y="4" width="12" height="8" fill="#fff" stroke="#777"/><rect x="8" y="18" width="12" height="8" fill="#fff" stroke="#777"/></svg>
  <svg width="30" height="28" viewBox="0 0 30 28"><rect x="2" y="7" width="26" height="17" fill="#f5e6b0" stroke="#a08a40"/><path d="M2 7 L15 17 L28 7" fill="none" stroke="#a08a40" stroke-width="1.5"/></svg>
</div>
<main class="article">
  <h1 class="article-title">NRTA Coffs Road Show Update</h1>
  <div class="meta">Written by Glen Harper</div>
  <div class="meta">Thursday, 07 July 2011 11:36</div>
  <p>This is a heads up regarding the upcoming NRTA Road Show event being held down<br>Coffs way on July 17.</p>
  <p>Entries have been coming in slowly and at last count were nudging the 50 mark but<br>there is still room for more so if you are planning on riding and haven't as yet advised us<br>of your intensions to do so then better get on to it and let me know as we don't<br>encourage unannounced non member surprises on the day.</p>
  <p>I have attached two versions of the Enrty Form, FYI, that can be downloaded, filled out,<br>presented and paid for on the day at Sign In but as metioned above, a heads up in<br>advance via <a href="#">nrta@ridgemail.com</a> is and would be much appreciated plus a good way of</p>
</main>
<aside class="sidebar">
  <div class="social-box"><div class="head">Social</div><div class="badge"></div></div>
  <div class="latest-head">Latest</div>
  <ul class="latest-list">
    <li class="bullet">Hell Trials</li>
    <li class="bullet">"Schedule</li>
    <li>$20.</li>
    <li class="bullet">Try a Trial</li>
    <li class="bullet">New Parts</li>
    <li>Footpegs</li>
    <li class="bullet">RENTALS</li>
  </ul>
</aside>
</body>
</html>
```